Velora Autohaus Nordic
Velora Autohaus Nordic - Automotive
Creative Brief
Modern
Velora Autohaus Nordic Oy
Автомобили и мототехника из США и Европы
info@veloraautohaus.example
www.veloraautohaus.example
The data that I would like to see: Velora Autohaus Nordic Oy Автомобили и мототехника из США и Европы (Cars and bikes from the U.S. and Europe) Контакты Phone: +7-918-647-20-83 (mobile phone) Skype: veloraautohaus Email: info@veloraautohaus.example www.veloraautohaus.example Генеральный директор (Director general) Белянский Артём Феликсович
On consideration of the developer. Will consider any options.

```html
<!DOCTYPE html>
<html lang="ru">
<head>
<meta charset="utf-8">
<title>Velora Autohaus Nordic — визитная карточка</title>
<link rel="stylesheet" href="https://fonts.googleapis.com/css2?family=Cormorant+SC:wght@500&family=PT+Serif:wght@400;700&display=swap">
<style>
  :root {
    --page-bg: #e9e6e2;
    --blue-bright: #37a8ec;
    --blue-mid: #1670b4;
    --navy: #0b1e33;
    --navy-deep: #050d17;
    --paper: #ffffff;
    --paper-shade: #e7eaee;
    --ink: #2b2f36;
    --ink-blue: #1d4f8f;
    --accent: #2b7fd0;
    --tagline: #a9d4f3;
  }
  * { box-sizing: border-box; margin: 0; padding: 0; }
  html, body { width: 1200px; height: 1070px; overflow: hidden; }
  body {
    background: var(--page-bg);
    display: flex;
    flex-direction: column;
    align-items: center;
    gap: 40px;
    padding-top: 35px;
  }
  .card {
    width: 820px;
    height: 480px;
    border-radius: 28px;
    overflow: hidden;
    position: relative;
    box-shadow: 0 6px 18px rgba(0,0,0,.18);
  }
  .blue-field {
    --flare-top: 62%;
    background:
      radial-gradient(ellipse 60% 22% at 45% var(--flare-top), rgba(255,255,255,.28), transparent 70%),
      linear-gradient(180deg, var(--blue-bright) 0%, var(--blue-mid) 45%, var(--navy) 66%, var(--navy-deep) 100%);
  }
  .blue-field::after {
    content: "";
    position: absolute;
    left: 0; right: 0; top: var(--flare-top);
    height: 2px;
    background: linear-gradient(90deg, transparent, rgba(255,255,255,.85) 45%, transparent);
  }
  .brand {
    position: absolute;
    display: flex;
    align-items: center;
    gap: 26px;
    z-index: 1;
  }
  .brand-mark {
    width: 92px; height: 92px;
    border-radius: 50%;
    border: 3px solid rgba(255,255,255,.9);
    flex: none;
  }
  .brand-name {
    font-family: "Cormorant SC", serif;
    font-weight: 500;
    color: #ffffff;
    line-height: .95;
    font-size: 58px;
  }
  .tagline {
    position: absolute;
    font-family: "PT Serif", serif;
    color: var(--tagline);
    letter-spacing: 2px;
    z-index: 1;
  }
  .card-front .brand { left: 110px; top: 150px; }
  .card-front .tagline { left: 226px; top: 330px; font-size: 19px; }

  .card-back { background: linear-gradient(180deg, var(--paper) 40%, var(--paper-shade) 100%); }
  .card-back .blue-field {
    --flare-top: 140px;
    position: absolute; left: 0; right: 0; top: 0; height: 210px;
  }
  .card-back .brand { left: 190px; top: 36px; gap: 18px; }
  .card-back .brand-mark { width: 62px; height: 62px; border-width: 2px; }
  .card-back .brand-name { font-size: 40px; }
  .card-back .tagline { left: 270px; top: 160px; font-size: 13px; }
  .contacts {
    position: absolute; left: 40px; top: 238px;
    font-family: "PT Serif", serif;
    color: var(--ink);
  }
  .company { font-size: 25px; color: var(--ink-blue); }
  .role { font-size: 14px; margin-top: 2px; }
  .rule { width: 320px; height: 3px; background: var(--accent); margin: 10px 0 16px; }
  .contact-list { list-style: none; }
  .contact-list li {
    display: flex; align-items: center; gap: 14px;
    font-size: 15px; height: 34px;
  }
  .contact-list svg { width: 18px; height: 18px; flex: none; }
</style>
</head>
<body>
  <section class="card card-front blue-field" aria-label="Лицевая сторона">
    <div class="brand">
      <span class="brand-mark"></span>
      <span class="brand-name">Velora Autohaus<br>Nordic</span>
    </div>
    <p class="tagline">Автомобили и мототехника из США и Европы</p>
  </section>

  <section class="card card-back" aria-label="Оборотная сторона">
    <div class="blue-field">
      <div class="brand">
        <span class="brand-mark"></span>
        <span class="brand-name">Velora Autohaus<br>Nordic</span>
      </div>
      <p class="tagline">Автомобили и мототехника из США и Европы</p>
    </div>
    <div class="contacts">
      <p class="company">Velora Autohaus Nordic Oy</p>
      <p class="role">Генеральный директор</p>
      <div class="rule"></div>
      <ul class="contact-list">
        <li>
          <svg viewBox="0 0 20 20"><circle cx="10" cy="10" r="9" fill="#4a5563"/><path d="M7 5.5l2 2.2-1 1.3c.7 1.4 1.6 2.3 3 3l1.3-1 2.2 2-1.2 1.6C9.6 14.3 5.7 10.4 5.4 6.7z" fill="#fff"/></svg>
          +7-918-647-20-83
        </li>
        <li>
          <svg viewBox="0 0 20 20"><circle cx="10" cy="10" r="9" fill="var(--accent)"/></svg>
          veloraautohaus
        </li>
        <li>
          <svg viewBox="0 0 20 20"><circle cx="10" cy="10" r="9" fill="#4a5563"/><rect x="5" y="6.5" width="10" height="7" fill="none" stroke="#fff" stroke-width="1.3"/><path d="M5 6.5l5 4 5-4" fill="none" stroke="#fff" stroke-width="1.3"/></svg>
          info@veloraautohaus.example
        </li>
        <li>
          <svg viewBox="0 0 20 20"><circle cx="10" cy="10" r="9" fill="#4a5563"/><path d="M5 10.5L10 6l5 4.5M6.5 9.5V14h7V9.5" fill="none" stroke="#fff" stroke-width="1.3"/></svg>
          www.veloraautohaus.example
        </li>
      </ul>
    </div>
  </section>
</body>
</html>
```